QRN Law Letterhead

Want law firm letterhead - both in terms of a pdf file that I can use electronically as letterhead by adding it as a background - and in terms of a file that I can send to a company to create actual letterhead.
Industry/Entity Type
Law Firm
Font styles to use
Sans Serif
Requirements
Must have
- Should have the following information (you can decide where to place):
- My name - Emil Vostrakian
- My email - emil@qrnlegalgroup.example
- My address - 2861 Corvella Parkway 318-742
- San Jose, California 95342
- Website - www.qrnlegalgroup.example
- Phone - 408-297-1586
- Fax - 408-853-2941
- The logo I attached
Nice to have
- I think I would prefer to have a black and white color scheme.
- I don't necessarily need a title after my name, but I have seen a few design submissions that include a generic title. The title I would use is "IP Litigator & Trademark Attorney"

```html
<!DOCTYPE html>
<html lang="en">
<head>
<meta charset="utf-8">
<title>QRN Law Letterhead</title>
<link rel="stylesheet" href="https://fonts.googleapis.com/css2?family=Lato:wght@400;700&family=Tinos:wght@400;700&display=swap">
<style>
  :root {
    --canvas: #e6e7e8;
    --paper: #fafafa;
    --brand: #5e7888;
    --swoosh: #a3a3a3;
    --watermark: #ededed;
    --ink: #2b2b2b;
    --on-brand: #ffffff;
  }
  html, body {
    margin: 0;
    width: 1200px;
    height: 1200px;
    overflow: hidden;
    background: var(--canvas);
  }
  .letterhead {
    position: absolute;
    left: 232px;
    top: 50px;
    width: 735px;
    height: 1100px;
    background: var(--paper);
    box-shadow: 0 6px 18px rgba(0,0,0,0.25);
    overflow: hidden;
    font-family: "Tinos", "Times New Roman", serif;
    color: var(--ink);
  }
  .letterhead__art {
    position: absolute;
    inset: 0;
    width: 100%;
    height: 100%;
  }
  .brand {
    position: absolute;
    left: 54px;
    top: 62px;
    display: flex;
    align-items: center;
    gap: 12px;
  }
  .brand__dot {
    width: 52px;
    height: 52px;
    border-radius: 50%;
    background: var(--brand);
  }
  .brand__name {
    font-family: "Lato", Arial, sans-serif;
    font-weight: 400;
    font-size: 46px;
    letter-spacing: 1px;
    color: var(--brand);
  }
  .sender {
    position: absolute;
    right: 45px;
    top: 36px;
    text-align: right;
    font-family: "Lato", Arial, sans-serif;
    color: var(--on-brand);
  }
  .sender__name {
    font-size: 20px;
    font-weight: 400;
    letter-spacing: 0.2px;
    line-height: 1.1;
  }
  .sender__email {
    font-size: 13.5px;
    line-height: 1.3;
  }
  .letter {
    position: absolute;
    left: 66px;
    width: 602px;
    font-size: 14.6px;
    line-height: 17.6px;
    margin: 0;
  }
  .letter--date { top: 224px; }
  .letter--recipient { top: 295px; }
  .letter--ref { top: 402px; font-weight: 700; }
  .letter--greeting { top: 473px; }
  .letter--para1 { top: 509px; text-align: justify; }
  .letter--para2 { top: 579px; text-align: justify; }
  .letter--ack { top: 651px; }
  .letter--closing { top: 722px; }
  .contact {
    position: absolute;
    left: 54px;
    top: 990px;
    font-family: "Lato", Arial, sans-serif;
    color: var(--on-brand);
    font-size: 15px;
    line-height: 18px;
  }
  .contact__line {
    display: flex;
    align-items: center;
    gap: 5px;
  }
  .contact__icon { width: 11px; height: 11px; }
  .contact__address {
    margin-top: 8px;
    font-size: 15.5px;
  }
</style>
</head>
<body>
<main class="letterhead">
  <svg class="letterhead__art" viewBox="0 0 653 978" preserveAspectRatio="none" aria-hidden="true">
    <circle cx="395" cy="520" r="205" fill="none" stroke="var(--watermark)" stroke-width="36"/>
    <path d="M235,0 C400,40 560,125 653,215 L653,0 Z" fill="var(--brand)"/>
    <path d="M310,26 C450,70 580,140 650,212" fill="none" stroke="var(--swoosh)" stroke-width="4"/>
    <path d="M0,758 C60,830 200,878 400,918 C520,942 600,955 653,968 L653,978 L0,978 Z" fill="var(--brand)"/>
    <path d="M30,782 C120,850 300,890 600,945" fill="none" stroke="var(--swoosh)" stroke-width="4"/>
  </svg>

  <div class="brand">
    <span class="brand__dot"></span>
    <span class="brand__name">QRN Law</span>
  </div>

  <div class="sender">
    <div class="sender__name">EMIL VOSTRAKIAN</div>
    <div class="sender__email">emil@qrnlegalgroup.example</div>
  </div>

  <p class="letter letter--date">Issuing date: May 5, 2012</p>
  <p class="letter letter--recipient">Name of employee: Mr. xyz<br>Address of employee<br>address line 2</p>
  <p class="letter letter--ref">Ref: Promotion as an Assistant secretary</p>
  <p class="letter letter--greeting">Dear Mr. xyz,</p>
  <p class="letter letter--para1">I have the pleasure to inform you that you have been promoted as assistant secretary in the share department of the company. You are required to take charge of the new assignment on 15<sup style="font-size:9px">th</sup> May, 2012. Please accept my hearty congratulations on your promotion.</p>
  <p class="letter letter--para2">Your salary scale in the promoted cadre will be Tk. 16,000 and from 15th may, your basic salary will be fixed at Tk. 12,000 in the said scale. You will be entitled to all other allowances as applicable to the staff-II of the company. Other services conditions remain unchanged.</p>
  <p class="letter letter--ack">Please acknowledge receipt of this letter.</p>
  <p class="letter letter--closing">Yours sincerely,</p>

  <div class="contact">
    <div class="contact__line">
      <svg class="contact__icon" viewBox="0 0 12 12"><path d="M1,4 C1,2 3,1 6,1 C9,1 11,2 11,4 L8.5,4.5 L8,3 L4,3 L3.5,4.5 Z M3,5 L9,5 L10,10 L2,10 Z" fill="var(--on-brand)"/></svg>
      <span>408-297-1586</span>
    </div>
    <div class="contact__line">
      <svg class="contact__icon" viewBox="0 0 12 12"><rect x="1" y="4" width="10" height="7" fill="var(--on-brand)"/><rect x="3" y="1" width="6" height="4" fill="none" stroke="var(--on-brand)" stroke-width="1.2"/><rect x="3" y="6" width="6" height="1" fill="var(--brand)"/></svg>
      <span>408-853-2941</span>
    </div>
    <div class="contact__line">
      <svg class="contact__icon" viewBox="0 0 12 12"><circle cx="6" cy="6" r="5" fill="var(--on-brand)"/><path d="M1,6 H11 M6,1 C3,4 3,8 6,11 C9,8 9,4 6,1" fill="none" stroke="var(--brand)" stroke-width="0.8"/></svg>
      <span>www.qrnlegalgroup.example</span>
    </div>
    <div class="contact__address">2861 Corvella Parkway 318-742 San Jose, California 95342</div>
  </div>
</main>
</body>
</html>
```